Smile club flyer design

I am launching an office smile club and would like a design that sits my branding and that is appealing to customers. I have a design (I need a new one) that has all the information.
My website is maplecrestdentalcarewv.com
Brand color is green. The design can be any color

Target Market(s)

Ages 30+

Industry/Entity Type

Dental

Font styles to use
Serif

Requirements
Must have
• Appealing to patients

```html
<!DOCTYPE html>
<html lang="en">
<head>
<meta charset="utf-8">
<title>Smile Club Membership – Maplecrest Dental Care</title>
<link rel="stylesheet" href="https://fonts.googleapis.com/css2?family=Playfair+Display:wght@700;900&family=Great+Vibes&family=Montserrat:wght@500;600;700;800&family=Rubik:wght@300;400;500&display=swap">
<style>
  :root{
    --teal:#1bb8a4;
    --teal-dark:#0f9a88;
    --teal-deep:#0b7d70;
    --brand-green:#1f8d3a;
    --navy:#1b2f6b;
    --ink:#2c2c2c;
    --mint:#bdeee6;
    --mint-light:#e2f7f3;
    --white:#ffffff;
  }
  *{margin:0;padding:0;box-sizing:border-box}
  html,body{width:846px;height:1200px;overflow:hidden;background:#ffffff}
  .flyer{position:relative;width:846px;height:1200px;overflow:hidden;
    background:linear-gradient(180deg,var(--white) 0,var(--white) 360px,var(--mint) 420px,#b7ece3 800px,var(--mint-light) 1200px);
    font-family:"Rubik",sans-serif;color:var(--ink)}
  .wave{position:absolute;left:0;top:330px;width:846px;height:110px}
  .leaf-accent{position:absolute;left:720px;top:312px;width:110px;height:72px;border-radius:50% 50% 40% 40%;
    background:radial-gradient(circle at 50% 60%,#1bb8a4 0,#27c2ad 55%,rgba(255,255,255,0) 72%)}
  .brand{position:absolute;top:46px;left:0;width:100%;text-align:center}
  .brand-name{font-family:"Playfair Display",serif;font-weight:700;font-size:42px;color:var(--brand-green);line-height:1}
  .brand-sub{margin-top:6px;font-family:"Montserrat",sans-serif;font-weight:700;font-size:15px;letter-spacing:5px;color:var(--brand-green);
    display:flex;justify-content:center;align-items:center;gap:8px}
  .brand-sub::before,.brand-sub::after{content:"";display:block;width:26px;height:2px;background:var(--brand-green)}
  .intro{position:absolute;top:138px;left:0;width:100%;text-align:center;font-family:"Great Vibes",cursive;font-size:64px;color:var(--navy);line-height:1;z-index:2}
  .title{position:absolute;top:180px;left:0;width:100%;text-align:center;font-family:"Playfair Display",serif;font-weight:900;font-size:86px;color:var(--teal);line-height:1;letter-spacing:-1px}
  .membership{position:absolute;top:270px;left:0;width:100%;text-align:center;font-family:"Montserrat",sans-serif;font-weight:600;font-size:28px;letter-spacing:9px;color:var(--navy)}
  .tagline{position:absolute;top:306px;left:0;width:100%;text-align:center;font-family:"Montserrat",sans-serif;font-weight:500;font-size:16px;color:var(--navy)}
  .tagline strong{color:var(--brand-green);font-weight:700}
  .plans{position:absolute;top:438px;left:83px;display:flex;gap:16px}
  .plan{position:relative;width:216px;height:420px;background:var(--white);border:1px solid var(--teal);border-radius:8px;overflow:hidden}
  .plan-head{height:64px;background:linear-gradient(180deg,var(--teal) 0,var(--teal-dark) 100%);color:var(--white);text-align:center;padding-top:10px}
  .plan-name{font-family:"Playfair Display",serif;font-weight:700;font-size:25px;line-height:1}
  .plan-type{font-family:"Montserrat",sans-serif;font-weight:600;font-size:12px;letter-spacing:.5px;margin-top:4px}
  .features{list-style:none;padding:14px 10px 0 12px}
  .features li{display:flex;gap:6px;font-size:16.5px;font-weight:300;line-height:1.3;margin-bottom:15px;color:#222}
  .features b{font-weight:500;color:var(--navy)}
  .tick{flex:none;width:13px;height:13px;margin-top:4px}
  .price{position:absolute;left:22px;bottom:0;width:170px;height:60px;border-radius:16px 16px 0 0;
    background:linear-gradient(180deg,var(--teal) 0,var(--teal-dark) 100%);color:var(--white);display:flex;align-items:center;justify-content:center;gap:4px}
  .price-amount{font-family:"Montserrat",sans-serif;font-weight:800;font-size:46px;line-height:1}
  .price-amount sup{font-size:20px;vertical-align:top;position:relative;top:4px}
  .price-term{font-family:"Montserrat",sans-serif;font-weight:700;font-size:14px;line-height:.95}
  .refresh{position:absolute;top:876px;left:73px;width:682px;height:76px;background:var(--white);border:2px solid var(--teal);border-radius:0 38px 38px 0;display:flex;align-items:center}
  .refresh-label{position:relative;width:196px;height:76px;margin:-2px 0 0 -2px;background:linear-gradient(180deg,var(--teal) 0,var(--teal-dark) 100%);border-radius:6px 0 0 6px;color:var(--white);padding:16px 0 0 17px;font-family:"Montserrat",sans-serif}
  .refresh-title{font-weight:800;font-size:26px;line-height:1}
  .refresh-sub{font-weight:700;font-size:13px;letter-spacing:.4px;margin-top:3px}
  .tag-new{position:absolute;top:-12px;right:0;background:var(--navy);color:var(--white);font-weight:600;font-size:14px;letter-spacing:.5px;padding:2px 9px;border-radius:8px 8px 0 8px;border:1.5px solid var(--white)}
  .refresh-items{display:flex;gap:26px;padding-left:18px;font-family:"Montserrat",sans-serif;font-weight:500;font-size:15px;line-height:1.3;color:#222}
  .refresh-items div{display:flex;gap:5px}
  .refresh-price{position:absolute;right:-33px;top:-4px;width:80px;height:80px;border-radius:50%;background:var(--teal-deep);color:var(--white);
    display:flex;align-items:center;justify-content:center;font-family:"Rubik",sans-serif;font-weight:500;font-size:26px}
  .refresh-price sup{font-size:12px;vertical-align:top;position:relative;top:-4px}
  .join{position:absolute;top:966px;left:129px;width:586px;height:44px;border-radius:22px;background:linear-gradient(90deg,var(--teal-dark),var(--teal));display:flex;align-items:center;padding:3px}
  .join-cta{height:38px;padding:0 22px;border-radius:19px;background:var(--navy);color:var(--white);display:flex;align-items:center;font-family:"Montserrat",sans-serif;font-weight:800;font-size:18.5px}
  .join-phone{display:flex;align-items:center;gap:6px;padding-left:12px;color:var(--white);font-family:"Montserrat",sans-serif;font-weight:800;font-size:26px}
  .phone-icon{width:20px;height:20px}
  .financing{position:absolute;top:1028px;left:0;width:100%;text-align:center}
  .financing-title{font-family:"Montserrat",sans-serif;font-weight:600;font-size:14px;letter-spacing:4.5px;color:#222}
  .partners{margin-top:10px;display:flex;justify-content:center;align-items:center;gap:16px;font-family:"Montserrat",sans-serif;font-weight:700;font-size:28px}
  .partner-lendwell{color:var(--teal-deep)}
  .partner-paybloom{color:#4a2b32}
  .partner-divider{width:1px;height:26px;background:#333}
  .plans-note{margin-top:22px;font-family:"Montserrat",sans-serif;font-weight:600;font-size:12px;color:var(--navy)}
  .fee-note{margin-top:4px;font-family:"Montserrat",sans-serif;font-weight:500;font-size:15px;color:#222}
  .fee-note span{color:var(--navy);font-weight:600}
  .website{position:absolute;bottom:24px;left:0;width:100%;text-align:center;font-family:"Montserrat",sans-serif;font-weight:600;font-size:13px;color:var(--teal-deep)}
</style>
</head>
<body>
<main class="flyer">
  <svg class="wave" viewBox="0 0 846 110" preserveAspectRatio="none" aria-hidden="true">
    <path d="M0 40 C120 -10 250 10 360 50 C470 90 580 95 690 70 C760 54 810 30 846 10 L846 110 L0 110 Z" fill="#bdeee6"/>
    <path d="M0 40 C120 -10 250 10 360 50 C470 90 580 95 690 70 C760 54 810 30 846 10" fill="none" stroke="#1bb8a4" stroke-width="10"/>
  </svg>
  <div class="leaf-accent" role="img" aria-label="Teal leaf sprig decoration"></div>

  <header class="brand">
    <div class="brand-name">Maplecrest</div>
    <div class="brand-sub">DENTAL CARE</div>
  </header>

  <div class="intro">Introducing</div>
  <h1 class="title">SMILE CLUB</h1>
  <div class="membership">MEMBERSHIP</div>
  <p class="tagline">Affordable dental care - <strong>No insurance required</strong></p>

  <section class="plans">
    <article class="plan">
      <div class="plan-head"><div class="plan-name">CORE CARE</div><div class="plan-type">PREVENTIVE</div></div>
      <ul class="features">
        <li><svg class="tick" viewBox="0 0 14 14"><circle cx="7" cy="7" r="7" fill="#1b2f6b"/><path d="M3.8 7.2l2.2 2.2 4.2-4.4" stroke="#fff" stroke-width="1.8" fill="none"/></svg><span>Comprehensive Annual Exam</span></li>
        <li><svg class="tick" viewBox="0 0 14 14"><circle cx="7" cy="7" r="7" fill="#1b2f6b"/><path d="M3.8 7.2l2.2 2.2 4.2-4.4" stroke="#fff" stroke-width="1.8" fill="none"/></svg><span>2 Professional Cleanings per Year</span></li>
        <li><svg class="tick" viewBox="0 0 14 14"><circle cx="7" cy="7" r="7" fill="#1b2f6b"/><path d="M3.8 7.2l2.2 2.2 4.2-4.4" stroke="#fff" stroke-width="1.8" fill="none"/></svg><span>Routine Bitewing X-rays</span></li>
        <li><svg class="tick" viewBox="0 0 14 14"><circle cx="7" cy="7" r="7" fill="#1b2f6b"/><path d="M3.8 7.2l2.2 2.2 4.2-4.4" stroke="#fff" stroke-width="1.8" fill="none"/></svg><span>10% Savings On treatment</span></li>
      </ul>
      <div class="price"><span class="price-amount"><sup>$</sup>39</span><span class="price-term">Per<br>Month</span></div>
    </article>
    <article class="plan">
      <div class="plan-head"><div class="plan-name">BRIGHT</div><div class="plan-type">COSMETIC</div></div>
      <ul class="features">
        <li><svg class="tick" viewBox="0 0 14 14"><circle cx="7" cy="7" r="7" fill="#1b2f6b"/><path d="M3.8 7.2l2.2 2.2 4.2-4.4" stroke="#fff" stroke-width="1.8" fill="none"/></svg><span>Annual In Office Whitening (Top &amp; Bottom)</span></li>
        <li><svg class="tick" viewBox="0 0 14 14"><circle cx="7" cy="7" r="7" fill="#1b2f6b"/><path d="M3.8 7.2l2.2 2.2 4.2-4.4" stroke="#fff" stroke-width="1.8" fill="none"/></svg><span>Custom Whitening Trays</span></li>
        <li><svg class="tick" viewBox="0 0 14 14"><circle cx="7" cy="7" r="7" fill="#1b2f6b"/><path d="M3.8 7.2l2.2 2.2 4.2-4.4" stroke="#fff" stroke-width="1.8" fill="none"/></svg><span><b>15%</b> Savings on Elective Treatment</span></li>
      </ul>
      <div class="price"><span class="price-amount"><sup>$</sup>59</span><span class="price-term">Per<br>Month</span></div>
    </article>
    <article class="plan">
      <div class="plan-head"><div class="plan-name">TOTAL SMILE</div><div class="plan-type">PERIODONTAL</div></div>
      <ul class="features">
        <li><svg class="tick" viewBox="0 0 14 14"><circle cx="7" cy="7" r="7" fill="#1b2f6b"/><path d="M3.8 7.2l2.2 2.2 4.2-4.4" stroke="#fff" stroke-width="1.8" fill="none"/></svg><span>3-4 Perio Maintenance Visits per Year</span></li>
        <li><svg class="tick" viewBox="0 0 14 14"><circle cx="7" cy="7" r="7" fill="#1b2f6b"/><path d="M3.8 7.2l2.2 2.2 4.2-4.4" stroke="#fff" stroke-width="1.8" fill="none"/></svg><span>1 Comprehensive Exam</span></li>
        <li><svg class="tick" viewBox="0 0 14 14"><circle cx="7" cy="7" r="7" fill="#1b2f6b"/><path d="M3.8 7.2l2.2 2.2 4.2-4.4" stroke="#fff" stroke-width="1.8" fill="none"/></svg><span>Diagnostic X-rays</span></li>
        <li><svg class="tick" viewBox="0 0 14 14"><circle cx="7" cy="7" r="7" fill="#1b2f6b"/><path d="M3.8 7.2l2.2 2.2 4.2-4.4" stroke="#fff" stroke-width="1.8" fill="none"/></svg><span><b>15%</b> Savings on Restorative &amp; Elective Care</span></li>
      </ul>
      <div class="price"><span class="price-amount"><sup>$</sup>89</span><span class="price-term">Per<br>Month</span></div>
    </article>
  </section>

  <section class="refresh">
    <div class="refresh-label">
      <span class="tag-new">NEW</span>
      <div class="refresh-title">SMILE</div>
      <div class="refresh-sub">REFRESH PACKAGE</div>
    </div>
    <div class="refresh-items">
      <div><svg class="tick" viewBox="0 0 14 14"><circle cx="7" cy="7" r="7" fill="#1b2f6b"/><path d="M3.8 7.2l2.2 2.2 4.2-4.4" stroke="#fff" stroke-width="1.8" fill="none"/></svg><span>Cleaning + Comprehensive<br>Exam + Whitening</span></div>
      <div><svg class="tick" viewBox="0 0 14 14"><circle cx="7" cy="7" r="7" fill="#1b2f6b"/><path d="M3.8 7.2l2.2 2.2 4.2-4.4" stroke="#fff" stroke-width="1.8" fill="none"/></svg><span>Limited<br>Time Offer</span></div>
    </div>
    <div class="refresh-price"><sup>$</sup>499</div>
  </section>

  <div class="join">
    <span class="join-cta">JOIN SMILE CLUB TODAY!</span>
    <span class="join-phone">
      <svg class="phone-icon" viewBox="0 0 20 20" aria-hidden="true"><circle cx="10" cy="10" r="8.5" fill="none" stroke="#fff" stroke-width="2"/><path d="M7 5.5l1.6 0 .8 2.3-1.1.9c.6 1.3 1.5 2.2 2.8 2.8l.9-1.1 2.3.8 0 1.6c0 .6-.5 1-1.1 1C9.6 13.6 6.4 10.4 6.2 6.6c0-.6.4-1.1.8-1.1z" fill="#fff"/></svg>
      304-555-0148
    </span>
  </div>

  <section class="financing">
    <div class="financing-title">FLEXIBLE FINANCING FOR TREATMENT</div>
    <div class="partners">
      <span class="partner-lendwell">LendWell</span>
      <span class="partner-divider"></span>
      <span class="partner-paybloom">PayBloom</span>
    </div>
    <div class="plans-note">PAYMENT PLANS AVAILABLE</div>
    <div class="fee-note">*<span>$49</span> Lifetime Activation Fee (Non-Refundable)</div>
  </section>

  <div class="website">maplecrestdentalcarewv.com</div>
</main>
</body>
</html>
```